I want a business card that is going to show a creative spark but without limiting me to an industry. Something edgy but that wont go out of date. I want it state My business name Serafina Loire, profession - Professional Makeup Artist contact number and email

My service is to provide makeup services from bridal, fashion, photography, film, TV and so on. It is creative and different so i want that to be reflected.

I would like the card double sided.
Updates

 I would LOVE a background on my card something like this image... i can supply an image to be formed like this

Please use the image uploaded

Can we try using the image provided on one side of the card and then writing and details on the other side

Target Market(s)

I am targeting a wide range of people from Creative directors to the individual eg. bride

Industry/Entity Type

Business

Requirements
Must have
• Name: Delphine Hartwell
contact numbe 0417853120
email address:info@serafinaloire.com
website: www.serafinaloire.com
One of the images attached

professional makeup artist / hair stylist

I want it to show creativity
Nice to have
• logo, Double-sided card
Should not have
• the design should not use tradional style. Or images that are not my own

```html
<!DOCTYPE html>
<html lang="en">
<head>
<meta charset="UTF-8">
<title>Serafina Loire — Business Card</title>
<link href="https://fonts.googleapis.com/css2?family=Jost:ital,wght@0,400;1,400&family=Satisfy&display=swap" rel="stylesheet">
<style>
  :root {
    --page: #ffffff;
    --card-dark: #3f2417;
    --card-mid: #5a3826;
    --card-light: #6b4631;
    --portrait-deep: #3a2112;
    --portrait-hair: #7d5836;
    --portrait-gold: #a7804f;
    --portrait-warm: #b88d6c;
    --label-tan: #c99b74;
    --subtitle-tan: #c6a58c;
    --text-light: #fbf6f1;
  }
  * { margin: 0; padding: 0; box-sizing: border-box; }
  html, body {
    width: 1200px;
    height: 900px;
    overflow: hidden;
    background: var(--page);
  }
  .canvas {
    position: relative;
    width: 1200px;
    height: 900px;
  }
  .business-card {
    position: absolute;
    left: 60px;
    top: 100px;
    width: 1080px;
    height: 600px;
    overflow: hidden;
    background:
      radial-gradient(ellipse 420px 300px at 760px 140px, rgba(120, 82, 60, 0.4), transparent 70%),
      radial-gradient(ellipse 380px 280px at 980px 480px, rgba(40, 20, 12, 0.3), transparent 70%),
      linear-gradient(120deg, var(--card-mid) 0%, var(--card-light) 45%, var(--card-mid) 75%, var(--card-dark) 100%);
  }
  .portrait-area {
    position: absolute;
    left: 0;
    top: 0;
    width: 560px;
    height: 600px;
    background:
      radial-gradient(ellipse 260px 340px at 300px 260px, rgba(184, 141, 108, 0.85), transparent 75%),
      radial-gradient(ellipse 200px 260px at 130px 470px, rgba(167, 128, 79, 0.8), transparent 75%),
      linear-gradient(160deg, var(--portrait-deep) 0%, var(--portrait-hair) 35%, var(--portrait-gold) 65%, var(--portrait-hair) 100%);
    -webkit-mask-image: linear-gradient(90deg, #000 72%, transparent 100%);
    mask-image: linear-gradient(90deg, #000 72%, transparent 100%);
  }
  .identity {
    position: absolute;
    right: 44px;
    top: 292px;
    text-align: right;
  }
  .identity__name {
    font-family: "Satisfy", cursive;
    font-size: 50px;
    font-weight: 400;
    color: var(--text-light);
    line-height: 1;
    letter-spacing: 1px;
  }
  .identity__role {
    margin-top: 4px;
    font-family: "Jost", sans-serif;
    font-style: italic;
    font-size: 24px;
    color: var(--subtitle-tan);
    letter-spacing: 0.5px;
  }
  .contact {
    position: absolute;
    right: 48px;
    top: 440px;
    text-align: right;
    font-family: "Jost", sans-serif;
    color: var(--text-light);
    list-style: none;
  }
  .contact__item {
    font-size: 27px;
    line-height: 40px;
  }
  .contact__label {
    color: var(--label-tan);
    margin-right: 6px;
  }
</style>
</head>
<body>
  <div class="canvas">
    <section class="business-card">
      <div class="portrait-area" role="img" aria-label="Painterly portrait photograph of a woman with long wavy hair and red lipstick"></div>

      <header class="identity">
        <h1 class="identity__name">Serafina Loire</h1>
        <p class="identity__role">Professional Makeup Artist</p>
      </header>

      <ul class="contact">
        <li class="contact__item"><span class="contact__label">m:</span>0417 853 120</li>
        <li class="contact__item"><span class="contact__label">e:</span>info@serafinaloire.com</li>
        <li class="contact__item"><span class="contact__label">w:</span>www.serafinaloire.com</li>
      </ul>
    </section>
  </div>
</body>
</html>
```